The Nine Lanterns CD cover and booklet - meditation walks

I have created a CD of five meditation walks for the modern mystic - with a professional voice over and really cool music - to help people find their way back home to their true Self. It is very powerful and life-enhancing. The walks were created on the Canary Island of Lanzarote in Bartolo's garden and I have stunning photographs taken by pro-photographer Owen Fairbrook to accompany the sleeve notes. The result will be a truly beautiful 12pp CD sleeve note booklet - which will itself be so cleanly laid out people will want to pick it up and play! :-) You can do that for me ... and, of course, you will get a free signed copy of the finished CD ... Rudy - The Nine Lanterns - see http://www.thewellspring-example.com/
I will send a CD page layout template, the full text and hi-res images to the selected design partner. I attach sample text docs and lo-res logo.
Extra guaranteed money and extended deadline with helpful files.
Hi there - I'm very excited about what designs I get for The Nine Lanterns CD. Everything is ready to go!
Rudy
Today I have uploaded a hi-res version of The Nine Lanterns logo which you may find helpful.
Rudy
Several designers have requested hi-res images of the pictures on the PDF sample pages - so I have uploaded this evening some additional hi-res images as well as a hi-res logo.
hi all you lovely designers! Today is the last day for submission of designs - so if you want a shout ... its now or never. :-)

```html
<!DOCTYPE html>
<html lang="en">
<head>
<meta charset="utf-8">
<title>The Nine Lanterns – CD Cover</title>
<link href="https://fonts.googleapis.com/css2?family=Crimson+Text:ital,wght@0,400;0,600;1,400&display=swap" rel="stylesheet">
<style>
  :root {
    --ink: #2b2a26;
    --ink-soft: #3d3b36;
    --white: #ffffff;
    --foam-top: #d9e2e3;
    --foam-mid: #eef2f1;
    --sand-pale: #efe9e3;
    --sand-deep: #8d7560;
    --sand-mid: #a88f78;
    --sea-band: #c9cfcf;
    --accent-orange: #e2631f;
  }
  * { margin: 0; padding: 0; box-sizing: border-box; }
  html, body { width: 1200px; height: 596px; overflow: hidden; background: var(--white); }
  body { font-family: "Crimson Text", Georgia, serif; color: var(--ink); }

  .cover { position: relative; width: 1200px; height: 596px; overflow: hidden; }

  .beach-backdrop {
    position: absolute; inset: 0;
    background:
      linear-gradient(180deg, rgba(255,255,255,0) 0%, rgba(255,255,255,0.35) 100%),
      linear-gradient(180deg, var(--foam-top) 0%, var(--foam-mid) 28%, #f3f1ed 55%, var(--sand-pale) 100%);
  }
  .panel { position: absolute; top: 0; height: 596px; width: 600px; }
  .panel--back { left: 0; }
  .panel--front { left: 600px; background: rgba(255,255,255,0.45); }

  .wordmark {
    position: absolute; left: 0; right: 0; text-align: center;
    font-weight: 600; letter-spacing: 0.04em; color: var(--ink);
  }
  .wordmark .dot {
    display: inline-block; border-radius: 50%; background: var(--accent-orange);
    vertical-align: middle;
  }
  .panel--back .wordmark { top: 106px; font-size: 24px; }
  .panel--back .wordmark .dot { width: 12px; height: 12px; margin-right: 8px; }
  .panel--front .wordmark { top: 68px; font-size: 44px; }
  .panel--front .wordmark .dot { width: 20px; height: 20px; margin-right: 12px; }

  .tracklist {
    position: absolute; top: 176px; left: 0; width: 600px;
    list-style: none; text-align: center;
    font-size: 19px; line-height: 29px; color: var(--ink);
  }
  .blurb {
    position: absolute; top: 376px; left: 0; width: 600px; text-align: center;
    font-size: 17.5px; line-height: 27px; color: var(--ink);
  }
  .copyright {
    position: absolute; top: 564px; left: 0; width: 600px; text-align: center;
    font-size: 13px; color: var(--ink-soft);
  }

  .tagline {
    position: absolute; top: 166px; left: 0; width: 600px; text-align: center;
    font-size: 21px; color: var(--ink);
  }
  .footprints-photo {
    position: absolute; top: 220px; left: 0; width: 600px; height: 272px;
    background:
      linear-gradient(180deg, var(--sea-band) 0%, #b9b2a8 14%, var(--sand-mid) 30%, var(--sand-deep) 70%, #7d6753 100%);
  }
  .quote {
    position: absolute; top: 300px; left: 60px; width: 490px; text-align: center;
    font-size: 20px; line-height: 26px; color: var(--white);
  }
  .quote cite {
    display: block; text-align: right; margin-top: 10px; padding-right: 20px;
    font-style: italic;
  }
  .paths {
    position: absolute; top: 462px; left: 0; width: 600px; text-align: center;
    font-size: 16.5px; color: var(--white); letter-spacing: 0.01em;
  }
  .credit {
    position: absolute; top: 512px; left: 0; width: 600px; text-align: center;
    font-size: 19px; line-height: 25px; color: var(--ink);
  }
</style>
</head>
<body>
<main class="cover">
  <div class="beach-backdrop" role="img" aria-label="Photograph of a pale beach with white sea foam and a distant figure walking at the water's edge"></div>

  <section class="panel panel--back">
    <div class="wordmark"><span class="dot"></span>THE NINE LANTERNS</div>
    <ol class="tracklist">
      <li>1. Introduction 3:52</li>
      <li>2. Via Positiva 9:04</li>
      <li>3. Via Negativa 6:54</li>
      <li>4. Via Creativa 6:22</li>
      <li>5. Via Transformativa 5:52</li>
      <li>6. Via Integrativa 4:53</li>
    </ol>
    <p class="blurb">These walking meditations created in Bartolo’s garden,<br>
      Lanzarote will make you feel grounded<br>
      and uplifted, centred and expansive, connected with your deepest<br>
      purpose and your true Self.</p>
    <p class="copyright">© Tidewell Publishing 2013</p>
  </section>

  <section class="panel panel--front">
    <div class="wordmark"><span class="dot"></span>THE NINE LANTERNS</div>
    <p class="tagline">walking meditations for the mystic in you</p>
    <div class="footprints-photo" role="img" aria-label="Photograph of footprints in wet sand leading along the shoreline"></div>
    <blockquote class="quote">
      “You find out that what you’ve been searching for<br>you already are.”
      <cite>Vance Merriton</cite>
    </blockquote>
    <p class="paths">Via Positiva • Via Negativa • Via Creativa • Via Transformativa • Via Interativa</p>
    <p class="credit">created by<br>Rudy Hallorand</p>
  </section>
</main>
</body>
</html>
```